Design a BOLD Ad Design for Fitness Club

We are fitness facility that is about to run our new "Bright Parent Reboot" program and we need a bold design created for an ad that will run on Instagram and Facebook.

The ad needs to be eye catching, easy to read and attractive so that someone stops scrolling and clicks to join.

The add needs to be sized to 1080 x 1080, include our logo and the text "Bright Parent Reboot" and "Starting September 23rd"

I have included an example photo, which is to be used as an example only of a design style that stands out to us, (colors, female photo style, etc)

I have also included our logo, which the yellow color can be changed for this design.

Thank you and we look forward to seeing your design.

```html
<!DOCTYPE html>
<html lang="en">
<head>
<meta charset="utf-8">
<title>IronVerve – Bright Parent Reboot</title>
<link rel="stylesheet" href="https://fonts.googleapis.com/css2?family=Russo+One&family=Orbitron:wght@700;900&family=Kaushan+Script&display=swap">
<style>
  :root {
    --bg: #050407;
    --white: #ffffff;
    --gold: #f5c400;
    --purple-deep: #2c0b4a;
    --purple: #6a1fa3;
    --purple-bright: #9a45d0;
    --magenta-glow: #c260d8;
    --spark: rgba(214, 170, 40, 0.32);
  }
  html, body {
    margin: 0;
    padding: 0;
    width: 1200px;
    height: 1200px;
    overflow: hidden;
    background: var(--bg);
  }
  .ad {
    position: relative;
    width: 1200px;
    height: 1200px;
    overflow: hidden;
    background: var(--bg);
  }
  .sparkle-field {
    position: absolute;
    left: 0;
    top: 430px;
    width: 760px;
    height: 770px;
    background: radial-gradient(ellipse at 35% 65%, var(--spark) 0%, rgba(214,170,40,0.1) 42%, rgba(0,0,0,0) 72%);
  }
  .athlete-photo {
    position: absolute;
    left: 390px;
    top: 20px;
    width: 810px;
    height: 1180px;
    border-radius: 380px 0 0 0;
    background:
      radial-gradient(ellipse 300px 360px at 66% 34%, var(--magenta-glow) 0%, rgba(194,96,216,0) 100%),
      linear-gradient(160deg, var(--purple-bright) 0%, var(--purple) 45%, var(--purple-deep) 100%);
    -webkit-mask-image: linear-gradient(90deg, rgba(0,0,0,0.25) 0%, #000 30%, #000 100%);
    mask-image: linear-gradient(90deg, rgba(0,0,0,0.25) 0%, #000 30%, #000 100%);
  }
  .brand {
    position: absolute;
    left: 125px;
    top: 140px;
    width: 572px;
    text-align: center;
  }
  .brand-name {
    font-family: "Russo One", sans-serif;
    font-size: 124px;
    line-height: 1.05;
    color: var(--white);
    letter-spacing: -1px;
  }
  .brand-tagline {
    margin-top: 12px;
    font-family: "Russo One", sans-serif;
    font-size: 21px;
    letter-spacing: 3px;
    color: var(--gold);
  }
  .headline {
    position: absolute;
    left: 108px;
    top: 525px;
    margin: 0;
    font-weight: normal;
  }
  .headline-line {
    display: block;
    font-family: "Orbitron", sans-serif;
    font-weight: 900;
    font-size: 104px;
    line-height: 1.0;
    color: var(--white);
    transform: skewX(-14deg);
    transform-origin: left bottom;
  }
  .headline-accent {
    display: block;
    margin-top: -6px;
    margin-left: 14px;
    font-family: "Kaushan Script", cursive;
    font-size: 118px;
    line-height: 1.05;
    color: var(--gold);
  }
  .start-date {
    position: absolute;
    left: 104px;
    top: 880px;
    margin: 0;
    font-family: "Orbitron", sans-serif;
    font-weight: 700;
    font-size: 40px;
    color: var(--white);
    transform: skewX(-14deg);
    transform-origin: left bottom;
  }
  .start-date sup {
    font-size: 22px;
    vertical-align: 18px;
  }
</style>
</head>
<body>
  <main class="ad">
    <div class="sparkle-field" role="img" aria-label="Scattered glowing gold bokeh particles"></div>
    <div class="athlete-photo" role="img" aria-label="Photo of a determined female athlete with a high ponytail in a purple fitted top, lit in violet light"></div>

    <header class="brand">
      <div class="brand-name">IronVerve</div>
      <div class="brand-tagline">PERSONAL GROUP TRAINING</div>
    </header>

    <h1 class="headline">
      <span class="headline-line">BRIGHT</span>
      <span class="headline-line">PARENT</span>
      <span class="headline-accent">reboot</span>
    </h1>

    <p class="start-date">Starting September 23<sup>rd</sup></p>
  </main>
</body>
</html>
```